beauty salon

providing waxing services from a home base this must include which I will provide a price list and an address

Industry/Entity Type

Beauty Salon

Font styles to use
Script

Colors

Designer to choose colors to be used in the design.

```html
<!DOCTYPE html>
<html lang="en">
<head>
<meta charset="utf-8">
<title>Serena's Bloom Salon – Waxing Flyer</title>
<link rel="stylesheet" href="https://fonts.googleapis.com/css2?family=Great+Vibes&family=Libre+Baskerville:ital,wght@0,400;0,700;1,400&display=swap">
<style>
  :root{
    --plum:#5b2a6e;
    --plum-deep:#4a1c5e;
    --magenta:#a51c7c;
    --magenta-light:#c02a8e;
    --teal:#4fc1b6;
    --yellow:#f7d613;
    --yellow-deep:#f0b400;
    --white:#ffffff;
    --ink:#2a1030;
    --logo:#8b1a6b;
    --photo-light:#f6f2ef;
    --photo-skin:#e2c1a8;
    --serif:'Libre Baskerville', Georgia, serif;
    --script:'Great Vibes', cursive;
  }
  *{margin:0;padding:0;box-sizing:border-box}
  html,body{width:851px;height:1200px;overflow:hidden;background:var(--white)}
  .flyer{position:relative;width:851px;height:1200px;overflow:hidden;font-family:var(--serif);color:var(--white)}
  .tagline-band{position:absolute;left:0;top:0;width:851px;height:46px;background:var(--plum);
    display:flex;align-items:center;justify-content:center;font-style:italic;font-size:29px;letter-spacing:.5px}
  .hero-photo{position:absolute;left:0;top:46px;width:851px;height:560px;
    background:radial-gradient(ellipse 55% 45% at 35% 40%, var(--photo-skin) 0%, #efdccd 45%, var(--photo-light) 80%)}
  .waves{position:absolute;left:0;top:0}
  .brand-name{position:absolute;left:468px;top:176px;font-weight:700;font-size:31px;color:var(--logo);white-space:nowrap}
  .discount-badge{position:absolute;left:44px;top:456px;width:180px;height:180px;border-radius:50%;
    background:radial-gradient(circle at 40% 35%, #fff36a 0%, var(--yellow) 45%, var(--yellow-deep) 100%);
    color:var(--ink);text-align:center;display:flex;flex-direction:column;justify-content:center;line-height:1}
  .discount-badge .pct{font-size:54px}
  .discount-badge .pct small{font-size:30px}
  .discount-badge .word{font-size:30px;margin-top:2px}
  .discount-badge .note{font-size:19px;margin-top:4px;line-height:1.1}
  .therapist{position:absolute;left:200px;top:580px;width:600px;text-align:center;font-family:var(--script);font-size:60px;line-height:1}
  .diploma{position:absolute;left:200px;top:648px;width:600px;text-align:center;font-weight:700;font-size:19px}
  .phone{position:absolute;left:265px;top:688px;display:flex;align-items:center;gap:12px;color:var(--yellow);font-size:47px}
  .phone svg{width:40px;height:40px}
  .info-line{position:absolute;left:200px;width:600px;text-align:center;font-weight:700;font-size:19px}
  .info-line .hl{color:var(--yellow)}
  .side-photo{position:absolute;left:0;width:204px}
  .side-photo.p1{top:708px;height:162px;background:linear-gradient(135deg,#e9d6ca,#f7efea 60%,#d9b9a5)}
  .side-photo.p2{top:876px;height:156px;background:linear-gradient(135deg,#c98e73,#e9cbb8 55%,#f3ece8)}
  .side-photo.p3{top:1038px;height:162px;background:linear-gradient(135deg,#f1e4dc,#d8ab93 55%,#f5efea)}
  .price-col{position:absolute;width:260px}
  .price-col.ladies{left:228px;top:864px}
  .price-col.extras{left:520px;top:864px}
  .price-head{height:24px;background:var(--plum-deep);border-radius:3px;text-align:center;font-weight:700;font-size:15px;line-height:24px;margin-bottom:10px}
  .price-list{list-style:none;font-size:12.5px}
  .price-list li{display:flex;align-items:baseline;height:18.4px}
  .price-list .item{white-space:nowrap}
  .price-list .dots{flex:1;border-bottom:1.5px dotted var(--white);margin:0 3px;transform:translateY(-3px)}
  .price-list .cost{white-space:nowrap}
  .mens{margin-top:12px}
  .book-now{position:absolute;left:518px;top:1156px;width:314px;height:27px;background:var(--yellow);
    color:var(--logo);font-weight:700;font-size:16px;text-align:center;line-height:27px}
</style>
</head>
<body>
<div class="flyer">
  <div class="tagline-band">fall in love with yourself. &nbsp;get smooth, hair-free skin</div>

  <div class="hero-photo" role="img" aria-label="Photo of smooth bare legs of a seated woman on a white background"></div>

  <svg class="waves" width="851" height="1200" viewBox="0 0 851 1200" aria-hidden="true">
    <defs>
      <linearGradient id="magentaFill" x1="0" y1="0" x2="0" y2="1">
        <stop offset="0" stop-color="#b5268a"/>
        <stop offset="1" stop-color="#9c1877"/>
      </linearGradient>
    </defs>
    <path d="M0,395 C70,455 140,510 260,548 L0,600 Z" fill="#5a2370"/>
    <path d="M851,412 C660,515 420,548 200,566 L200,610 L851,610 Z" fill="#4fc1b6"/>
    <path d="M0,592 C260,578 600,548 851,490 L851,1200 L0,1200 Z" fill="url(#magentaFill)"/>
  </svg>

  <div class="brand-name">Serena's Bloom Salon</div>

  <div class="discount-badge">
    <div class="pct">10<small>%</small></div>
    <div class="word">discount</div>
    <div class="note">on first<br>treatment.</div>
  </div>

  <div class="therapist">Beauty Therapist Serena</div>
  <div class="diploma">Diploma of Beauty Therapy at Marlow Hart</div>

  <div class="phone">
    <svg viewBox="0 0 40 40" aria-hidden="true">
      <circle cx="20" cy="20" r="18" fill="none" stroke="#ffffff" stroke-width="2.5"/>
      <path d="M14 10c-2 1-3 3-2 6 2 6 6 10 12 13 3 1 5 0 6-2l-4-4-3 2c-3-1-5-4-6-6l2-3z" fill="#ffffff"/>
    </svg>
    <span>0400 555 019</span>
  </div>

  <div class="info-line" style="top:751px">Address: &nbsp;12 Finch Lane, Eastbrook</div>
  <div class="info-line" style="top:785px"><span class="hl">Now open:</span> Wednesday 10am – 4pm</div>
  <div class="info-line" style="top:820px">Fridays 10am-7pm &nbsp;| &nbsp;Saturday 10am -4pm</div>

  <div class="side-photo p1" role="img" aria-label="Photo of a leg being waxed with a wax strip"></div>
  <div class="side-photo p2" role="img" aria-label="Photo of eyebrow waxing treatment"></div>
  <div class="side-photo p3" role="img" aria-label="Photo of chest waxing with a wax strip"></div>

  <div class="price-col ladies">
    <div class="price-head">Lady's Waxing</div>
    <ul class="price-list">
      <li><span class="item">Eyebrow</span><span class="dots"></span><span class="cost">$8</span></li>
      <li><span class="item">Upper lip</span><span class="dots"></span><span class="cost">$8</span></li>
      <li><span class="item">Chin</span><span class="dots"></span><span class="cost">$8</span></li>
      <li><span class="item">Face wax</span><span class="dots"></span><span class="cost">$25</span></li>
      <li><span class="item">Bikini line</span><span class="dots"></span><span class="cost">$15</span></li>
      <li><span class="item">G string</span><span class="dots"></span><span class="cost">$20</span></li>
      <li><span class="item">½ Brazilian</span><span class="dots"></span><span class="cost">$30</span></li>
      <li><span class="item">Full Brazilian</span><span class="dots"></span><span class="cost">$40</span></li>
      <li><span class="item">Half arm</span><span class="dots"></span><span class="cost">$20</span></li>
      <li><span class="item">Upper half arm</span><span class="dots"></span><span class="cost">$20</span></li>
      <li><span class="item">Full arm</span><span class="dots"></span><span class="cost">$25</span></li>
      <li><span class="item">Half leg</span><span class="dots"></span><span class="cost">$15</span></li>
      <li><span class="item">Upper leg</span><span class="dots"></span><span class="cost">$20</span></li>
      <li><span class="item">¾ Leg</span><span class="dots"></span><span class="cost">$25</span></li>
      <li><span class="item">Full leg</span><span class="dots"></span><span class="cost">$35</span></li>
    </ul>
  </div>

  <div class="price-col extras">
    <div class="price-head">Eye Enhancement</div>
    <ul class="price-list">
      <li><span class="item">Eyebrow tint</span><span class="dots"></span><span class="cost">$12</span></li>
      <li><span class="item">Eyelash tint</span><span class="dots"></span><span class="cost">$15</span></li>
    </ul>
    <div class="price-head mens">Mens Waxing</div>
    <ul class="price-list">
      <li><span class="item">Eyebrow</span><span class="dots"></span><span class="cost">$10</span></li>
      <li><span class="item">Half arm</span><span class="dots"></span><span class="cost">$20</span></li>
      <li><span class="item">Upper half arm</span><span class="dots"></span><span class="cost">$25</span></li>
      <li><span class="item">Full arm</span><span class="dots"></span><span class="cost">$30</span></li>
      <li><span class="item">Half leg</span><span class="dots"></span><span class="cost">$25</span></li>
      <li><span class="item">Full leg</span><span class="dots"></span><span class="cost">$45</span></li>
      <li><span class="item">Chest wax</span><span class="dots"></span><span class="cost">$40</span></li>
      <li><span class="item">Back wax</span><span class="dots"></span><span class="cost">$35</span></li>
    </ul>
  </div>

  <div class="book-now">Book your Appointment now!</div>
</div>
</body>
</html>
```